43 Year Old Construction firm needs Updated Business Card & Stationery Design

We are an established and well known (in our market) commercial construction firm. We need a cleaner and more modern look for our corporate identity material. We would like to continue to use our current colors and logo.
We are thinking about incorporating a slogan on our business card (either front or back): "Building lasting value for every client we serve." The text could change at some point. Our website is www.kvoplarn.com . Sample card is attached. Some will have more phone numbers, etc...
Updates

Target Market(s)

Commercial and institutional clients.

Industry/Entity Type

Construction Company

Contact Information for Business Card

See attached for existing card. But don't be constrained.

Requirements
Must have
• Logo, name, title, address, website, email, phone numbers (as few as one, as many as three)
• Slogan on front or back "Striving to be the most trusted builder in our market"
• Use existing logo and colors

```html
<!DOCTYPE html>
<html lang="en">
<head>
<meta charset="utf-8">
<title>Kvoplarn Constructors – Business Card</title>
<link rel="stylesheet" href="https://fonts.googleapis.com/css2?family=Arimo:wght@400;700&display=swap">
<style>
  :root {
    --navy: #123f7e;
    --navy-deep: #0b2f63;
    --green: #2aa55a;
    --ink: #3d3d3d;
    --paper: #ffffff;
    --backdrop: #ece9e4;
    --slogan: #dfe7f3;
  }
  * { margin: 0; padding: 0; box-sizing: border-box; }
  html, body {
    width: 1200px; height: 950px; overflow: hidden;
    background: var(--backdrop);
    font-family: "Arimo", Arial, sans-serif;
  }
  .canvas {
    width: 1200px; height: 950px;
    display: flex; flex-direction: column; align-items: center; justify-content: center;
    gap: 70px;
  }
  .card {
    width: 600px; height: 343px; position: relative; overflow: hidden;
    box-shadow: 0 10px 28px rgba(0,0,0,.22);
  }

  /* Back */
  .card-back {
    background: linear-gradient(135deg, var(--navy) 0%, var(--navy-deep) 100%);
    color: var(--paper);
  }
  .card-back .wordmark {
    position: absolute; left: 0; right: 0; top: 118px;
    text-align: center; font-weight: 700; font-size: 40px; letter-spacing: 2px;
    color: var(--paper);
  }
  .card-back .rule {
    position: absolute; left: 170px; right: 170px; top: 178px; height: 4px; background: var(--green);
  }
  .card-back .slogan {
    position: absolute; left: 0; right: 0; top: 206px; text-align: center;
    font-size: 15px; letter-spacing: .3px; color: var(--slogan);
  }

  /* Front */
  .card-front { background: var(--paper); }
  .brand {
    position: absolute; left: 44px; top: 92px; width: 260px;
    display: flex; align-items: center; gap: 12px;
  }
  .brand-square { width: 22px; height: 22px; background: var(--navy); flex: none; }
  .brand-name {
    font-weight: 700; font-size: 22px; line-height: 1.15; letter-spacing: 1px; color: var(--navy);
  }
  .divider {
    position: absolute; left: 318px; top: 66px; width: 1px; height: 150px;
    background: linear-gradient(to bottom, transparent, #c7c7c7 30%, #c7c7c7 70%, transparent);
  }
  .contact { position: absolute; left: 342px; top: 72px; color: var(--ink); }
  .contact .name { font-size: 21px; font-weight: 700; color: var(--navy); }
  .contact .title { font-size: 15px; color: var(--green); margin-bottom: 12px; }
  .contact p { font-size: 15px; line-height: 1.35; }
  .contact .line { display: flex; align-items: center; gap: 7px; }
  .contact svg { width: 14px; height: 14px; fill: var(--navy); flex: none; }

  .band {
    position: absolute; left: 0; right: 0; bottom: 34px; height: 58px;
    background: var(--navy); border-top: 3px solid var(--green);
    display: flex; align-items: center; justify-content: center;
  }
  .band .web { color: var(--paper); font-size: 16px; letter-spacing: 4px; }
  .band-edge {
    position: absolute; left: 0; right: 0; bottom: 22px; height: 2px; background: var(--green);
  }
</style>
</head>
<body>
<main class="canvas">
  <section class="card card-back" aria-label="Card back">
    <div class="wordmark">KVOPLARN</div>
    <div class="rule"></div>
    <p class="slogan">Building lasting value for every client we serve.</p>
  </section>

  <section class="card card-front" aria-label="Card front">
    <div class="brand">
      <span class="brand-square"></span>
      <span class="brand-name">KVOPLARN<br>CONSTRUCTORS</span>
    </div>
    <div class="divider"></div>
    <div class="contact">
      <div class="name">Alan Mercer</div>
      <div class="title">President</div>
      <p>2418 larkin avenue</p>
      <p>harlow park, KS 66210</p>
      <p class="line">
        <svg viewBox="0 0 24 24" aria-hidden="true"><path d="M6.6 10.8a15 15 0 0 0 6.6 6.6l2.2-2.2a1 1 0 0 1 1-.25 11.4 11.4 0 0 0 3.6.57 1 1 0 0 1 1 1V20a1 1 0 0 1-1 1A17 17 0 0 1 3 4a1 1 0 0 1 1-1h3.5a1 1 0 0 1 1 1c0 1.25.2 2.45.57 3.57a1 1 0 0 1-.25 1z"/></svg>
        913.555.0142
      </p>
      <p class="line">
        <svg viewBox="0 0 24 24" aria-hidden="true"><path d="M2 5h20v14H2V5zm2 2v.4l8 5 8-5V7H4z"/></svg>
        name@kvoplarn.com
      </p>
    </div>
    <div class="band"><span class="web">www.kvoplarn.com</span></div>
    <div class="band-edge"></div>
  </section>
</main>
</body>
</html>
```